Cookie needs a website

We need a website for a cookie company based in Mexico City. Our company (called Hornos Lucero) has been baking and crating all sorts of cookies and cakes for more than 35 years.
We started off as a family business and till this date we are still functioning as one. We need the design of the web to be more on the baking side as we have many types of cookies cakes, pastries & muffins. Key elements, home style baking, use colours black, white and red. Tabs we need: front page, who are we, our brands and contact Preferable in Spanish. Im sure you have questions, please contact us. This is for homepage PSD design only no CSS,XHTML or full website build or coding involved as this is design competition.
Updates

Some more information has been added. Thanks is advance for your talent!

Target Market(s)

Target is general public, mostly families. Our product is not a luxury good,more like an affordable treat, however we do use very high quality products and high quality standards. Our motive is natural ingredients and home baked goods.
Our main point of sales is having shops inside department stores. Our own shops and selling to other businesses for re sale

Industry/Entity Type

Business

Font styles to use
Serif

Colors
ec2027
ffffff
333333

Requirements
Must have
• Baking oriented. An oven would be nice since we bake in front of our clients.
Colors we use also important
Nice to have
• make it home. (you have design freedom)
Below are the logos HL is the company name. Pimbos is one of our branches and the the pictures are from the cookies we make
Should not have
• PLEASE NO corny, over colorfull or tacky designs!!

```html
<!DOCTYPE html>
<html lang="es">
<head>
<meta charset="utf-8">
<title>Hornos Lucero</title>
<link href="https://fonts.googleapis.com/css2?family=Cinzel:wght@400;700&family=Oswald:wght@400;500&family=Lato:ital,wght@0,400;0,700;1,400&display=swap" rel="stylesheet">
<style>
:root{
  --red:#ec2027;
  --red-dark:#d11a20;
  --ink:#333333;
  --ink-deep:#2a2a2a;
  --white:#ffffff;
  --paper:#e4dfd1;
  --paper-light:#efeeec;
  --muted:#555555;
  --grey-line:#cfcfcf;
}
*{box-sizing:border-box;margin:0;padding:0}
html,body{width:730px;height:1200px;overflow:hidden}
body{position:relative;background:var(--paper-light);font-family:'Lato',sans-serif;color:var(--ink)}
.abs{position:absolute}

/* header */
.hero{left:0;top:0;width:730px;height:365px;background:radial-gradient(ellipse at 60% 40%,#ece8dc 0%,var(--paper) 70%,#d9d3c2 100%)}
.top-social{top:8px;left:516px;display:flex;gap:8px}
.top-social span{width:17px;height:17px;border-radius:50%;background:#7a7a7a;display:block}
.top-phone{top:9px;left:575px;font-size:12px;color:#6a6a6a;display:flex;align-items:center;gap:6px}
.nav-ribbon{left:50px;top:28px}
.nav{top:56px;font-family:'Oswald',sans-serif;font-size:16px;color:var(--white);letter-spacing:.2px}
.brand-seal{left:307px;top:12px;width:116px;height:116px;border-radius:50%;background:var(--red);border:7px solid var(--ink);display:flex;align-items:center;justify-content:center;font-family:'Cinzel',serif;font-size:40px;color:var(--white)}
.hero-photo{left:0;top:112px;width:286px;height:196px;border-radius:46% 40% 44% 52%;background:radial-gradient(ellipse at 50% 45%,#d8c7a0 0%,#a88456 55%,#6b4526 100%)}
.since{top:178px;left:550px;font-family:'Cinzel',serif;font-size:13px;color:var(--ink);display:flex;align-items:center;gap:6px}
.since b{background:var(--red);color:var(--white);font-family:'Lato',sans-serif;font-size:12px;padding:0 3px;line-height:14px}
.headline{top:202px;left:312px;font-family:'Cinzel',serif;font-size:29px;line-height:33px;color:var(--ink);letter-spacing:.5px}
.headline em{font-style:normal;color:var(--red)}

/* categories */
.cat-panel{left:72px;top:338px;width:586px;height:204px;background:var(--white);box-shadow:0 2px 6px rgba(0,0,0,.15)}
.card{top:345px;width:182px;height:190px;background:var(--ink)}
.card .tag{position:absolute;left:0;top:0;width:28px;height:40px;background:var(--red);clip-path:polygon(0 0,100% 0,100% 100%,50% 82%,0 100%);color:var(--white);font-family:'Cinzel',serif;font-size:10px;text-align:center;padding-top:8px}
.card h3{position:absolute;left:38px;top:7px;font-family:'Oswald',sans-serif;font-weight:500;font-size:15px;color:var(--white)}
.card .photo{position:absolute;left:7px;top:50px;width:168px;height:76px;border:1px solid #c9b99a}
.card p{position:absolute;left:7px;top:138px;width:170px;font-size:9.5px;line-height:12px;color:var(--white)}
.card .edge{position:absolute;left:0;bottom:-5px}

.section-title{left:0;width:730px;text-align:center;font-family:'Oswald',sans-serif;font-size:22px;color:var(--muted)}
.divider{left:255px;width:220px;height:1px;background:var(--grey-line)}
.divider::after{content:"";position:absolute;left:104px;top:-3px;width:7px;height:7px;border-radius:50%;border:1px solid #aaa;background:var(--paper-light)}

.brand-box{top:626px;width:182px;height:68px;border:1px dashed #777;display:flex;align-items:center;justify-content:center;gap:8px}
.brand-name{font-family:'Cinzel',serif;font-weight:700;font-size:17px}
.brand-dot{width:46px;height:46px;border-radius:50%;background:#111}

.arrow-btn{top:808px;width:19px;height:27px;background:#222;border-radius:2px}
.product{top:770px;width:130px;height:103px;box-shadow:0 2px 4px rgba(0,0,0,.25)}
.product .photo{height:83px}
.product .label{height:20px;background:linear-gradient(#f0343a,var(--red-dark));color:var(--white);font-weight:700;font-size:10.5px;text-align:center;line-height:20px}

/* testimonial */
.testimonial{left:0;top:900px;width:730px;height:177px;background:var(--white)}
.avatar{left:337px;top:925px;width:56px;height:56px;border-radius:50%;border:3px solid #e6e6e6;background:radial-gradient(circle,#b59a86 0%,#7b6a5e 100%)}
.quote{left:100px;top:994px;width:530px;text-align:center;font-style:italic;font-size:8px;line-height:12px;color:#666}
.qmark{font-family:'Cinzel',serif;font-size:26px;color:var(--ink);font-weight:700}
.author{top:1025px;left:0;width:730px;text-align:center;color:var(--red);font-weight:700;font-size:9px}
.dots{top:1051px;left:341px;display:flex;gap:5px}
.dots span{width:6px;height:6px;border-radius:50%;background:var(--ink)}
.dots span:first-child{background:var(--red)}

/* info bar */
.info-bar{left:0;top:1077px;width:730px;height:56px;background:linear-gradient(#f0363c,var(--red-dark))}
.info-sep{top:1077px;width:1px;height:56px;background:rgba(255,255,255,.35)}
.hours-title{left:81px;top:1083px;font-family:'Cinzel',serif;font-size:12px;color:var(--white);display:flex;align-items:center;gap:8px}
.hours-text{left:81px;top:1104px;font-size:8.5px;line-height:13px;color:var(--white)}
.shop{left:258px;top:1098px;width:222px;text-align:center;font-family:'Cinzel',serif;font-size:14px;color:var(--white)}
.foot-social{left:540px;top:1096px;display:flex;gap:6px}
.foot-social span{width:17px;height:17px;border-radius:50%;background:var(--white)}

/* footer */
.footer{left:0;top:1133px;width:730px;height:67px;background:var(--ink-deep)}
.foot-links{left:81px;top:1146px;font-size:8.5px;color:var(--white)}
.foot-phone{left:360px;top:1142px;font-family:'Cinzel',serif;font-size:15px;color:#ddd;display:flex;align-items:center;gap:6px}
.foot-mail{left:563px;top:1146px;font-size:8.5px;color:var(--white);display:flex;align-items:center;gap:5px}
.foot-rule{left:0;top:1171px;width:730px;border-top:1px dashed #555}
.copyright{left:0;top:1182px;width:730px;text-align:center;font-size:8px;color:#aaa}
</style>
</head>
<body>

<header>
  <div class="abs hero"></div>
  <div class="abs top-social"><span></span><span></span></div>
  <div class="abs top-phone">
    <svg width="10" height="12" viewBox="0 0 10 12"><path d="M2 0h2l1 3-1.5 1.2c.6 1.6 1.6 2.8 3 3.5L8 6.5l2 1v2.3C10 11 9 12 8 12 3.5 11 0 7 0 2 0 1 1 0 2 0z" fill="#6a6a6a"/></svg>
    555 20 1934
  </div>
  <svg class="abs nav-ribbon" width="630" height="76" viewBox="0 0 630 76">
    <path d="M0 6 L60 14 L50 40 L62 62 L8 50 L22 28Z" fill="#2e2e2e"/>
    <path d="M630 6 L570 14 L580 40 L568 62 L622 50 L608 28Z" fill="#2e2e2e"/>
    <path d="M40 14 Q315 32 590 14 L582 62 Q315 78 48 62Z" fill="var(--ink)"/>
  </svg>
  <nav>
    <span class="abs nav" style="left:110px">HOME</span>
    <span class="abs nav" style="left:165px;top:61px">QUIENES SOMOS</span>
    <span class="abs nav" style="left:440px;top:61px">NUESTRAS MARCAS</span>
    <span class="abs nav" style="left:566px">CONTACTO</span>
  </nav>
  <div class="abs brand-seal">HL</div>
  <div class="abs hero-photo" role="img" aria-label="Galletas horneadas partidas a la mitad con pasas y nueces"></div>
  <div class="abs since">
    <svg width="22" height="12" viewBox="0 0 22 12"><path d="M1 11 Q6 3 20 4 M15 0 L20 4 L15 8" stroke="var(--ink)" stroke-width="1.6" fill="none"/></svg>
    SINCE <b>1977</b>
  </div>
  <h1 class="abs headline" style="font-weight:400">Horneando parausted<br>desde hace <em>35</em> años</h1>
</header>

<section class="categories">
  <div class="abs cat-panel"></div>
  <article class="abs card" style="left:80px">
    <div class="tag">HL</div><h3>COOKIES</h3>
    <div class="photo" role="img" aria-label="Galletas de avena en un plato" style="background:linear-gradient(135deg,#c9a06a,#8a5c30)"></div>
    <p>Lorem ipsum dolor sit amet, consectetuer adipiscing elit sed diam nonummy nibh euismod</p>
    <svg class="edge" width="182" height="6"><path d="M0 0 h182 v1 l-4 5 l-4-5 l-4 5 l-4-5 l-4 5 l-4-5 l-4 5 l-4-5 l-4 5 l-4-5 l-4 5 l-4-5 l-4 5 l-4-5 l-4 5 l-4-5 l-4 5 l-4-5 l-4 5 l-4-5 l-4 5 l-4-5 l-4 5 l-4-5 l-4 5 l-4-5 l-4 5 l-4-5 l-4 5 l-4-5 l-4 5 l-4-5 l-4 5 l-4-5 l-4 5 l-4-5 l-4 5 l-4-5 l-4 5 l-4-5 l-4 5 l-4-5 l-4 5 l-4-5 l-4 5 l-4-5 l-4 5 l-4-5 l-4 5 l-4-5 l-4 5 l-4-5 l-4 5 l-4-5 l-4 5 l-2-3Z" fill="var(--ink)"/></svg>
  </article>
  <article class="abs card" style="left:274px">
    <div class="tag">HL</div><h3>CAKES</h3>
    <div class="photo" role="img" aria-label="Variedad de pasteles sobre una mesa" style="background:linear-gradient(135deg,#b89a7c,#6e4a33)"></div>
    <p>Lorem ipsum dolor sit amet, consectetuer adipiscing elit sed diam nonummy nibh euismod</p>
    <svg class="edge" width="182" height="6"><path d="M0 0 h182 v1 l-4 5 l-4-5 l-4 5 l-4-5 l-4 5 l-4-5 l-4 5 l-4-5 l-4 5 l-4-5 l-4 5 l-4-5 l-4 5 l-4-5 l-4 5 l-4-5 l-4 5 l-4-5 l-4 5 l-4-5 l-4 5 l-4-5 l-4 5 l-4-5 l-4 5 l-4-5 l-4 5 l-4-5 l-4 5 l-4-5 l-4 5 l-4-5 l-4 5 l-4-5 l-4 5 l-4-5 l-4 5 l-4-5 l-4 5 l-4-5 l-4 5 l-4-5 l-4 5 l-4-5 l-4 5 l-4-5 l-4 5 l-4-5 l-4 5 l-4-5 l-4 5 l-4-5 l-4 5 l-4-5 l-4 5 l-2-3Z" fill="var(--ink)"/></svg>
  </article>
  <article class="abs card" style="left:467px">
    <div class="tag">HL</div><h3>PASTRIES &amp; MUFFINS</h3>
    <div class="photo" role="img" aria-label="Postres con frutos rojos y chocolate" style="background:linear-gradient(135deg,#d9b640,#8a1c24 60%,#2c1a1a)"></div>
    <p>Lorem ipsum dolor sit amet, consectetuer adipiscing elit sed diam nonummy nibh euismod</p>
    <svg class="edge" width="182" height="6"><path d="M0 0 h182 v1 l-4 5 l-4-5 l-4 5 l-4-5 l-4 5 l-4-5 l-4 5 l-4-5 l-4 5 l-4-5 l-4 5 l-4-5 l-4 5 l-4-5 l-4 5 l-4-5 l-4 5 l-4-5 l-4 5 l-4-5 l-4 5 l-4-5 l-4 5 l-4-5 l-4 5 l-4-5 l-4 5 l-4-5 l-4 5 l-4-5 l-4 5 l-4-5 l-4 5 l-4-5 l-4 5 l-4-5 l-4 5 l-4-5 l-4 5 l-4-5 l-4 5 l-4-5 l-4 5 l-4-5 l-4 5 l-4-5 l-4 5 l-4-5 l-4 5 l-4-5 l-4 5 l-4-5 l-4 5 l-4-5 l-4 5 l-2-3Z" fill="var(--ink)"/></svg>
  </article>
</section>

<section class="brands">
  <h2 class="abs section-title" style="top:562px;font-weight:400">OUR BRANDS</h2>
  <div class="abs divider" style="top:598px"></div>
  <div class="abs brand-box" style="left:80px"><span class="brand-name" style="color:#111">Pimbos</span></div>
  <div class="abs brand-box" style="left:274px"><span class="brand-name" style="color:var(--red)">Dalia's</span></div>
  <div class="abs brand-box" style="left:468px"><span class="brand-dot"></span><span class="brand-name" style="color:#111;font-size:14px">Hornos Lucero</span></div>
</section>

<section class="popular">
  <h2 class="abs section-title" style="top:719px;font-weight:400">POPULAR PRODUCT</h2>
  <div class="abs divider" style="top:754px"></div>
  <svg class="abs arrow-btn" style="left:44px" viewBox="0 0 19 27"><path d="M6 9v9 M13 10l-4 3.5 4 3.5" stroke="#fff" stroke-width="1.5" fill="none"/></svg>
  <svg class="abs arrow-btn" style="left:667px" viewBox="0 0 19 27"><path d="M6 9v9 M9 10l4 3.5-4 3.5" stroke="#fff" stroke-width="1.5" fill="none"/></svg>
  <div class="abs product" style="left:80px"><div class="photo" role="img" aria-label="Pastel de queso con chocolate y frambuesa" style="background:linear-gradient(135deg,#f1e6d8,#3b1e14 70%,#b8202a)"></div><div class="label">Lorem ipsum dolor</div></div>
  <div class="abs product" style="left:227px"><div class="photo" role="img" aria-label="Muffins con betún de crema" style="background:linear-gradient(160deg,#f3ead9,#a8783f 60%,#5a3a20)"></div><div class="label">Consectetuer</div></div>
  <div class="abs product" style="left:373px"><div class="photo" role="img" aria-label="Rebanada de pastel de chocolate con crema" style="background:linear-gradient(160deg,#5a7a3a,#3a1e12 45%,#efe8df 70%,#3a1e12)"></div><div class="label">Adipiscing Elit</div></div>
  <div class="abs product" style="left:519px"><div class="photo" role="img" aria-label="Galletas de jengibre decoradas" style="background:linear-gradient(135deg,#c9a98a,#9a4e26 60%,#7a3a1c)"></div><div class="label">Nibh Euismod</div></div>
  <svg class="abs" style="left:0;top:896px" width="730" height="6"><path d="M0 6 L0 3 l5-3 5 3 5-3 5 3 5-3 5 3 5-3 5 3 5-3 5 3 5-3 5 3 5-3 5 3 5-3 5 3 5-3 5 3 5-3 5 3 5-3 5 3 5-3 5 3 5-3 5 3 5-3 5 3 5-3 5 3 5-3 5 3 5-3 5 3 5-3 5 3 5-3 5 3 5-3 5 3 5-3 5 3 5-3 5 3 5-3 5 3 5-3 5 3 5-3 5 3 5-3 5 3 5-3 5 3 5-3 5 3 5-3 5 3 5-3 5 3 5-3 5 3 5-3 5 3 5-3 5 3 5-3 5 3 5-3 5 3 5-3 5 3 5-3 5 3 5-3 5 3 5-3 5 3 5-3 5 3 5-3 5 3 5-3 5 3 5-3 5 3 5-3 5 3 5-3 5 3 5-3 5 3 5-3 5 3 5-3 5 3 5-3 5 3 5-3 5 3 5-3 5 3 5-3 5 3 5-3 5 3 5-3 5 3 5-3 5 3 5-3 5 3 5-3 5 3 5-3 5 3 5-3 5 3 5-3 5 3 5-3 5 3 5-3 5 3 5-3 5 3 5-3 5 3 5-3 5 3 5-3 5 3 5-3 5 3 5-3 5 3 5-3 5 3 5-3 5 3 5-3 5 3 5-3 5 3 5-3 5 3 5-3 5 3 5-3 5 3 5-3 5 3 5-3 5 3 5-3 5 3 5-3 5 3 5-3 5 3 5-3 5 3 5-3 5 3 5-3 5 3 5-3 5 3 5-3 5 3 5-3 5 3 5-3 5 3 5-3 5 3 5-3 5 3 5-3 5 3 5-3 5 3 5-3 5 3 5-3 5 3 5-3 5 3 5-3 5 3 5-3 5 3 5-3 5 3 5-3 5 3 5-3 5 3 5-3 5 3 V6Z" fill="var(--white)"/></svg>
</section>

<section>
  <div class="abs testimonial"></div>
  <div class="abs avatar" role="img" aria-label="Retrato de la clienta Marta Ríos"></div>
  <span class="abs qmark" style="left:80px;top:984px">“</span>
  <p class="abs quote">Lorem ipsum dolor sit amet, consectetuer adipiscing elit, sed diam nonummy nibh euismod tincidunt ut laoreet dolore magna aliquam erat volutpat. Ut wisi enim ad minim veniam, quis nostrud exerci tation ullamcorper suscipit lobortis nisl ut aliquip ex ea commodo consequat.</p>
  <span class="abs qmark" style="left:558px;top:1002px">”</span>
  <p class="abs author">- Marta Ríos</p>
  <div class="abs dots"><span></span><span></span><span></span><span></span><span></span></div>
</section>

<section>
  <div class="abs info-bar"></div>
  <div class="abs info-sep" style="left:257px"></div>
  <div class="abs info-sep" style="left:480px"></div>
  <div class="abs hours-title">HORAS
    <svg width="18" height="18" viewBox="0 0 18 18"><circle cx="9" cy="9" r="7.5" stroke="#fff" stroke-width="1.6" fill="none"/><path d="M9 4v5h4" stroke="#fff" stroke-width="1.6" fill="none"/></svg>
  </div>
  <p class="abs hours-text">Horario de lunes a sábado de &nbsp;- <b>8:00 a 19:00</b><br><b>Domingo cerrado</b></p>
  <p class="abs shop">Tienda on line</p>
  <div class="abs foot-social"><span></span><span></span><span></span><span></span><span></span></div>
</section>

<footer>
  <div class="abs footer"></div>
  <p class="abs foot-links">HOME &nbsp;| &nbsp;QUIENES SOMOS &nbsp;| NUESTRAS MARCAS &nbsp;| CONTACTO</p>
  <div class="abs foot-phone">
    <svg width="10" height="16" viewBox="0 0 10 16"><rect x="1" y="1" width="8" height="14" rx="1.5" stroke="#ddd" stroke-width="1.4" fill="none"/><path d="M3 4h4M3 7h4M3 10h4" stroke="#ddd"/></svg>
    1-800-555-0199
  </div>
  <div class="abs foot-mail">
    <svg width="11" height="8" viewBox="0 0 11 8"><rect width="11" height="8" fill="#ddd"/><path d="M0 0l5.5 4.5L11 0" stroke="#2a2a2a" fill="none"/></svg>
    hola@hornoslucero.com
  </div>
  <div class="abs foot-rule"></div>
  <p class="abs copyright">© Copyright 2014 Hornos Lucero. All right reserved</p>
</footer>

</body>
</html>
```